Delphine Marchetti Photography
Letterhead & Business Card Design
Delphine Marchetti Photography - Photography
Creative Brief
Professional
Delphine Marchetti
Photographer / Owner
517 Bramble Lane Fort McMurray, AB T9K 2P6
delphinemarchettiphotography@pixmail.example
www.delphinemarchettiphotography.example
I think I'd like to include a photo I've taken...thoughts?

```html
<!DOCTYPE html>
<html lang="en">
<head>
<meta charset="utf-8">
<title>Delphine Marchetti Photography – Business Card</title>
<link rel="stylesheet" href="https://fonts.googleapis.com/css2?family=Open+Sans:wght@400;600;700&display=swap">
<style>
  :root {
    --backdrop: #2b2b2b;
    --card-white: #ffffff;
    --brand-blue: #0e97c6;
    --brand-blue-deep: #0a86b2;
    --brand-brown: #7a4e33;
    --text-light: #ffffff;
    --text-soft: #e6f6fc;
  }
  html, body {
    margin: 0;
    padding: 0;
    width: 1200px;
    height: 780px;
    overflow: hidden;
    background: var(--backdrop);
    font-family: "Open Sans", Arial, sans-serif;
  }
  .canvas {
    position: relative;
    width: 1200px;
    height: 780px;
  }
  .business-card {
    position: absolute;
    left: 100px;
    top: 104px;
    width: 1000px;
    height: 572px;
    border-radius: 34px;
    overflow: hidden;
    background: var(--card-white);
  }
  .card-bands {
    position: absolute;
    inset: 0;
    width: 100%;
    height: 100%;
  }
  .brand-mark {
    position: absolute;
    left: 120px;
    top: 88px;
    display: flex;
    align-items: center;
    gap: 30px;
  }
  .brand-mark__circle {
    width: 150px;
    height: 150px;
    border-radius: 50%;
    border: 6px solid var(--brand-brown);
    box-sizing: border-box;
  }
  .brand-mark__name {
    font-size: 44px;
    font-weight: 400;
    color: var(--brand-brown);
    letter-spacing: 0.5px;
    line-height: 1.15;
  }
  .owner-details {
    position: absolute;
    right: 545px;
    top: 384px;
    text-align: right;
    color: var(--text-light);
  }
  .owner-details__name {
    font-size: 27px;
    font-weight: 700;
    margin: 0 0 6px;
  }
  .owner-details__title {
    font-size: 20px;
    margin: 0 0 22px;
  }
  .owner-details__address {
    font-size: 20px;
    line-height: 1.35;
    margin: 0;
    font-style: normal;
  }
  .card-divider {
    position: absolute;
    left: 478px;
    top: 378px;
    width: 2px;
    height: 160px;
    background: var(--text-soft);
  }
  .contact-list {
    position: absolute;
    left: 502px;
    top: 376px;
    margin: 0;
    padding: 0;
    list-style: none;
    color: var(--text-light);
    font-size: 19px;
  }
  .contact-list__item {
    display: flex;
    align-items: center;
    gap: 14px;
    height: 36px;
  }
  .contact-list__icon {
    width: 20px;
    height: 20px;
    flex: none;
  }
</style>
</head>
<body>
<main class="canvas">
  <section class="business-card" aria-label="Business card">
    <svg class="card-bands" viewBox="0 0 1000 572" preserveAspectRatio="none" aria-hidden="true">
      <path d="M0 322 C 220 300, 420 372, 640 350 C 820 332, 920 292, 1000 272 L1000 572 L0 572 Z" fill="var(--brand-brown)"/>
      <path d="M0 344 C 220 322, 420 392, 640 368 C 820 350, 920 310, 1000 292 L1000 572 L0 572 Z" fill="var(--brand-blue)"/>
    </svg>

    <div class="brand-mark">
      <div class="brand-mark__circle" aria-hidden="true"></div>
      <div class="brand-mark__name">Delphine Marchetti<br>Photography</div>
    </div>

    <div class="owner-details">
      <p class="owner-details__name">Delphine Marchetti</p>
      <p class="owner-details__title">Photographer / Owner</p>
      <address class="owner-details__address">517 Bramble Lane<br>Fort McMurray, AB T9K 2P6</address>
    </div>

    <div class="card-divider" aria-hidden="true"></div>

    <ul class="contact-list">
      <li class="contact-list__item">
        <svg class="contact-list__icon" viewBox="0 0 20 20" aria-hidden="true"><path d="M5 2 L8 6 L6.5 8 C7.5 10.5 9.5 12.5 12 13.5 L14 12 L18 15 L16 18 C9 18 2 11 2 4 Z" fill="#fff"/></svg>
        <span>780.555.0142</span>
      </li>
      <li class="contact-list__item">
        <svg class="contact-list__icon" viewBox="0 0 20 20" aria-hidden="true"><rect x="5" y="2" width="10" height="6" fill="#fff"/><rect x="2" y="8" width="16" height="10" rx="2" fill="#fff"/><rect x="6" y="11" width="8" height="2" fill="var(--brand-blue)"/></svg>
        <span>780.555.0187</span>
      </li>
      <li class="contact-list__item">
        <svg class="contact-list__icon" viewBox="0 0 20 20" aria-hidden="true"><circle cx="10" cy="10" r="8" fill="#fff"/><text x="10" y="14.5" font-size="12" font-weight="700" text-anchor="middle" fill="var(--brand-blue)" font-family="Open Sans, sans-serif">@</text></svg>
        <span>delphinemarchettiphotography@pixmail.example</span>
      </li>
      <li class="contact-list__item">
        <svg class="contact-list__icon" viewBox="0 0 20 20" aria-hidden="true"><circle cx="10" cy="10" r="8" fill="#fff"/><ellipse cx="10" cy="10" rx="3.5" ry="8" fill="none" stroke="var(--brand-blue)" stroke-width="1.2"/><line x1="2" y1="10" x2="18" y2="10" stroke="var(--brand-blue)" stroke-width="1.2"/></svg>
        <span>www.delphinemarchettiphotography.example</span>
      </li>
    </ul>
  </section>
</main>
</body>
</html>
```